Criação de Kit Layout de Posts para Redes Sociais (Facebook, Instagram e etc) para Construção & Engenharia
A empresa queria:
" TRABALHAMOS COM LOCAÇÃO, VENDA DE EQUIPAMENTOS, MONTAGEM E PROJETOS DE ANDAIME E ESCORAMENTO "

```html
<!DOCTYPE html>
<html lang="pt-BR">
<head>
<meta charset="UTF-8">
<title>Vertix Equipamentos — Segurança e Confiança</title>
<link href="https://fonts.googleapis.com/css2?family=Montserrat:wght@300;400;600;700;800&display=swap" rel="stylesheet">
<style>
  :root {
    --bg-dark: #262626;
    --bg-mid: #333333;
    --gold: #f3c21b;
    --gold-deep: #c98f0a;
    --gold-light: #ffe27a;
    --ink: #2a2a2a;
    --white: #ffffff;
    --muted: #d9d9d9;
    --photo-top: #8fb8dc;
    --photo-mid: #d9cdb0;
    --photo-low: #8a7558;
  }
  * { margin: 0; padding: 0; box-sizing: border-box; }
  html, body { width: 1200px; height: 1200px; overflow: hidden; background: var(--bg-dark); }
  .post {
    position: relative;
    width: 1200px;
    height: 1200px;
    overflow: hidden;
    font-family: "Montserrat", sans-serif;
    background: radial-gradient(circle at 80% 30%, var(--bg-mid) 0%, var(--bg-dark) 70%);
  }
  .hero-photo-frame {
    position: absolute;
    left: 0; top: 0;
    width: 668px; height: 968px;
    border-bottom-right-radius: 250px;
    border-right: 3px solid var(--gold);
    border-bottom: 3px solid var(--gold);
    opacity: 0.85;
  }
  .hero-photo {
    position: absolute;
    left: 0; top: 0;
    width: 650px; height: 950px;
    border-bottom-right-radius: 232px;
    background: linear-gradient(180deg, var(--photo-top) 0%, var(--photo-mid) 55%, var(--photo-low) 100%);
  }
  .social-handle {
    position: absolute;
    top: 28px; right: 26px;
    display: flex; align-items: center; gap: 10px;
    color: var(--white);
    font-size: 21px; font-weight: 600; letter-spacing: 1px;
  }
  .social-handle .mark {
    width: 22px; height: 22px; background: var(--gold); border-radius: 4px;
  }
  .badge-shield {
    position: absolute;
    left: 835px; top: 315px;
    width: 175px; height: 195px;
    filter: drop-shadow(0 12px 18px rgba(0,0,0,0.45));
  }
  .headline-pill {
    position: absolute;
    left: 612px; top: 588px;
    width: 564px; height: 96px;
    background: var(--gold);
    border-radius: 20px;
    display: flex; align-items: center; justify-content: center;
    color: var(--ink);
    font-size: 72px; font-weight: 700; letter-spacing: 1px;
  }
  .headline-sub {
    position: absolute;
    right: 36px; top: 700px;
    color: var(--white);
    font-size: 76px; font-weight: 300; letter-spacing: 1px;
    line-height: 1.1;
  }
  .badge-shield--blurred {
    position: absolute;
    left: 700px; top: 860px;
    width: 320px; height: 356px;
    filter: blur(7px);
    transform: rotate(-8deg);
    opacity: 0.95;
  }
  .brand {
    position: absolute;
    left: 48px; top: 1010px;
  }
  .brand-lockup { display: flex; align-items: center; gap: 16px; }
  .brand-square { width: 92px; height: 92px; background: var(--gold); }
  .brand-name { color: var(--white); font-weight: 600; line-height: 1; }
  .brand-name .name { display: block; font-size: 66px; letter-spacing: 2px; }
  .brand-name .descriptor { display: block; font-size: 21px; letter-spacing: 6px; margin-top: 6px; }
  .brand-partners {
    margin-top: 20px;
    color: var(--muted);
    font-size: 20px; font-weight: 600; letter-spacing: 1px;
  }
</style>
</head>
<body>
<main class="post">
  <div class="hero-photo-frame"></div>
  <div class="hero-photo" role="img" aria-label="Foto de trabalhador com capacete e colete refletivo montando andaime metálico sob céu azul"></div>

  <div class="social-handle"><span class="mark"></span>@VERTIXEQUIPAMENTOS</div>

  <svg class="badge-shield" viewBox="0 0 100 112" aria-hidden="true">
    <defs>
      <linearGradient id="shieldGold" x1="0" y1="0" x2="1" y2="1">
        <stop offset="0" stop-color="#ffe27a"/>
        <stop offset="0.5" stop-color="#f3c21b"/>
        <stop offset="1" stop-color="#c98f0a"/>
      </linearGradient>
    </defs>
    <path d="M50 3 L94 18 V52 C94 82 73 100 50 109 C27 100 6 82 6 52 V18 Z" fill="#b57e08"/>
    <path d="M50 11 L86 23 V53 C86 77 69 92 50 100 C31 92 14 77 14 53 V23 Z" fill="url(#shieldGold)"/>
    <polyline points="32,56 45,69 69,42" fill="none" stroke="#ffffff" stroke-width="8" stroke-linecap="round" stroke-linejoin="round"/>
  </svg>

  <div class="headline-pill">+SEGURANÇA</div>
  <div class="headline-sub">+CONFIANÇA</div>

  <svg class="badge-shield--blurred" viewBox="0 0 100 112" aria-hidden="true">
    <defs>
      <linearGradient id="shieldGoldSoft" x1="0" y1="0" x2="1" y2="1">
        <stop offset="0" stop-color="#ffe27a"/>
        <stop offset="0.5" stop-color="#f3c21b"/>
        <stop offset="1" stop-color="#c98f0a"/>
      </linearGradient>
    </defs>
    <path d="M50 3 L94 18 V52 C94 82 73 100 50 109 C27 100 6 82 6 52 V18 Z" fill="#b57e08"/>
    <path d="M50 11 L86 23 V53 C86 77 69 92 50 100 C31 92 14 77 14 53 V23 Z" fill="url(#shieldGoldSoft)"/>
    <polyline points="32,56 45,69 69,42" fill="none" stroke="#ffffff" stroke-width="8" stroke-linecap="round" stroke-linejoin="round"/>
  </svg>

  <footer class="brand">
    <div class="brand-lockup">
      <span class="brand-square"></span>
      <span class="brand-name"><span class="name">VERTIX</span><span class="descriptor">EQUIPAMENTOS</span></span>
    </div>
    <div class="brand-partners">ALTUS ANDAIMES | FERROMAQ</div>
  </footer>
</main>
</body>
</html>
```